I need a business Card Design for my practice , i am clinical herbalist. I am a herbalist specializing in Lyme disease, autism, autoimmune diseases, difficult to cure diseasesDifficult to cure diseases. In my innovative practice i link traditional medicine, herbs with science, immunologu ,pharmacology.

Industry/Entity Type

Business

Contact Information for Business Card

My company name : OŚRODEK ZIELNIK
My name : Piotr Kaleta
Name of my profession : Fitoterapeuta
In Polish language Fitoterapeuta is Herbalist .

e-mail: piotrkaleta@osrodekzielnik.com
www.osrodek-zielnik.pl
phone : 604 587 231
My company adress : Dąbrowa Sitnicka 41 , 38-415 Lużna
I dont have logo .

Requirements
Nice to have
• My company

```html
<!DOCTYPE html>
<html lang="pl">
<head>
<meta charset="utf-8">
<title>Ośrodek Zielnik – wizytówka</title>
<link rel="stylesheet" href="https://fonts.googleapis.com/css2?family=Oswald:wght@400;500;700&family=Playfair+Display:wght@900&display=swap">
<style>
  :root {
    --backdrop: #000000;
    --band-green: #a6ff2e;
    --body-green: #ccff6b;
    --footer-green: #9cff12;
    --ink-blue: #0f1f9e;
    --ink-black: #111111;
    --herb-dark: #6b8f2a;
    --herb-light: #d89b4a;
  }
  html, body {
    margin: 0;
    padding: 0;
    width: 1200px;
    height: 1000px;
    overflow: hidden;
    background: var(--backdrop);
  }
  .canvas {
    position: relative;
    width: 1200px;
    height: 1000px;
  }
  .card {
    position: absolute;
    left: 350px;
    top: 60px;
    width: 500px;
    height: 880px;
    background: var(--body-green);
    font-family: "Oswald", "Arial Narrow", sans-serif;
    text-align: center;
    overflow: hidden;
  }
  .card__top-band {
    position: absolute;
    left: 0; top: 0;
    width: 100%;
    height: 48px;
    background: var(--band-green);
  }
  .card__company {
    position: absolute;
    left: 0; top: 36px;
    width: 100%;
    margin: 0;
    font-family: "Playfair Display", "Times New Roman", serif;
    font-weight: 900;
    font-size: 44px;
    line-height: 1;
    color: var(--ink-blue);
    transform: scaleX(0.82);
    letter-spacing: 0.5px;
  }
  .card__profession {
    position: absolute;
    left: 0; top: 86px;
    width: 100%;
    margin: 0;
    font-weight: 400;
    font-size: 32px;
    line-height: 1.3;
    color: var(--ink-black);
  }
  .card__herb-visual {
    position: absolute;
    left: 150px;
    top: 180px;
    width: 200px;
    height: 220px;
  }
  .card__note {
    position: absolute;
    left: 0; top: 420px;
    width: 100%;
    margin: 0;
    font-size: 25px;
    line-height: 1.35;
    color: var(--ink-black);
  }
  .card__name {
    position: absolute;
    left: 0; top: 628px;
    width: 100%;
    margin: 0;
    font-weight: 700;
    font-size: 48px;
    line-height: 1.2;
    letter-spacing: 1px;
    color: var(--ink-blue);
  }
  .card__phone {
    position: absolute;
    left: 0; top: 690px;
    width: 100%;
    margin: 0;
    font-size: 26px;
    line-height: 1.4;
    color: var(--ink-blue);
  }
  .card__footer {
    position: absolute;
    left: 0; bottom: 0;
    width: 100%;
    height: 136px;
    background: var(--footer-green);
  }
  .card__contacts {
    list-style: none;
    margin: 0;
    padding: 18px 0 0;
    font-size: 24px;
    line-height: 1.4;
    color: var(--ink-black);
  }
</style>
</head>
<body>
<main class="canvas">
  <article class="card">
    <div class="card__top-band"></div>
    <h1 class="card__company">OŚRODEK ZIELNIK</h1>
    <p class="card__profession">Fitoterapeuta</p>

    <svg class="card__herb-visual" viewBox="0 0 200 220" role="img" aria-label="Photo of a wooden mortar and pestle filled with fresh green herbs">
      <defs>
        <radialGradient id="herbTones" cx="50%" cy="50%" r="55%">
          <stop offset="0%" stop-color="#d89b4a"/>
          <stop offset="55%" stop-color="#6b8f2a"/>
          <stop offset="100%" stop-color="#ccff6b" stop-opacity="0"/>
        </radialGradient>
      </defs>
      <rect x="0" y="0" width="200" height="220" fill="url(#herbTones)"/>
    </svg>

    <p class="card__note">In Polish language Fitoterapeuta<br>is Herbalist</p>

    <h2 class="card__name">PIOTR KALETA</h2>
    <p class="card__phone">604 587 231</p>

    <footer class="card__footer">
      <ul class="card__contacts">
        <li>e-mail: piotrkaleta@osrodekzielnik.com</li>
        <li>www.osrodek-zielnik.pl</li>
        <li>Dąbrowa Sitnicka 41 , 38-415 Olszyny Górne</li>
      </ul>
    </footer>
  </article>
</main>
</body>
</html>
```